Business card for Full Stable Care Vandorpe

I would like to have me designed an professional business card with my existing logo for my company called : full stable care vandorpe gcv.
I prefer a two sided business card with on the back side only the horses head and the website : fscvandorpe-example.eu
Only one colour shouldbe all right.
The logo must appear in a nic professional way on the business card.

Other suggestion are welcome.

All copy wrights must be released by the designer after we have selected a final design.

Target Market(s)

Equestrian businesses

Industry/Entity Type

Business

Contact Information for Business Card

Laurent Vandorpe
Title: zaakvoerder
Full Stable Care Vandorpe GCV
Molkenweg 47
B - 2820 Bonheiden
België
Phone: + 32 491 68 27 04
Mail: laurent@fscvandorpe-example.eu

Font styles to use
Serif

Requirements
Must have
• My own logo
• See attached files
• Website: fscvandorpe-example.eu

```html
<!DOCTYPE html>
<html lang="nl">
<head>
<meta charset="utf-8">
<title>Full Stable Care Vandorpe – Business Card</title>
<link href="https://fonts.googleapis.com/css2?family=Tinos:wght@400;700&family=Lato:wght@400;700&display=swap" rel="stylesheet">
<style>
  :root {
    --page-bg: #eeebec;
    --card-dark: #1f1e1f;
    --card-dark-edge: #2b2a2b;
    --card-light: #ffffff;
    --ink: #141414;
    --ink-soft: #3a3a3a;
    --emblem-dark: #2e2d2e;
    --emblem-light: #ececec;
    --on-dark: #f4f4f4;
  }
  * { box-sizing: border-box; margin: 0; padding: 0; }
  html, body { width: 1200px; height: 1200px; overflow: hidden; }
  body {
    background: var(--page-bg);
    display: flex;
    flex-direction: column;
    align-items: center;
    justify-content: center;
    gap: 60px;
    font-family: "Lato", sans-serif;
  }
  .card {
    position: relative;
    width: 840px;
    height: 480px;
    border-radius: 36px;
    overflow: hidden;
    box-shadow: 0 10px 30px rgba(0,0,0,0.18);
  }
  /* back side */
  .card--back {
    background: radial-gradient(ellipse at 60% 30%, var(--card-dark-edge), var(--card-dark) 70%);
  }
  .card--back .emblem {
    position: absolute;
    left: 40px; bottom: -40px;
    width: 420px; height: 460px;
    border-radius: 50% 45% 40% 50%;
    background: linear-gradient(160deg, var(--emblem-dark), #262526);
  }
  .card--back .website {
    position: absolute;
    right: 34px; top: 50%;
    transform: translateY(-50%) rotate(90deg);
    transform-origin: center;
    color: var(--on-dark);
    font-size: 26px;
    letter-spacing: 1px;
    white-space: nowrap;
    width: 0;
    display: flex;
    justify-content: center;
  }
  /* front side */
  .card--front {
    background: linear-gradient(120deg, #f4f4f4, var(--card-light) 55%);
    color: var(--ink);
  }
  .card--front .emblem {
    position: absolute;
    left: 30px; bottom: -50px;
    width: 400px; height: 440px;
    border-radius: 50% 45% 40% 50%;
    background: linear-gradient(160deg, var(--emblem-light), #f2f2f2);
  }
  .card-details {
    position: absolute;
    right: 56px; top: 44px;
    text-align: right;
    display: flex;
    flex-direction: column;
    align-items: flex-end;
  }
  .brand {
    display: flex;
    align-items: center;
    gap: 12px;
    font-family: "Tinos", serif;
    font-weight: 700;
    font-size: 34px;
    text-transform: uppercase;
    letter-spacing: 0.5px;
  }
  .brand-dot { width: 22px; height: 22px; border-radius: 50%; background: var(--ink); }
  .person-name {
    margin-top: 22px;
    font-family: "Tinos", serif;
    font-weight: 700;
    font-size: 27px;
    letter-spacing: 1px;
    text-transform: uppercase;
  }
  .person-title { font-size: 20px; color: var(--ink-soft); }
  .contact { margin-top: 26px; font-size: 21px; line-height: 1.35; color: var(--ink-soft); }
  .company { margin-top: 24px; font-size: 21px; line-height: 1.35; color: var(--ink-soft); }
  .company strong { color: var(--ink); font-weight: 700; }
</style>
</head>
<body>
  <section class="card card--back" aria-label="Achterzijde visitekaart">
    <div class="emblem" role="img" aria-label="Groot paardenhoofd-embleem, subtiel donkergrijs op zwart"></div>
    <p class="website"><span>www. fscvandorpe-example.eu</span></p>
  </section>

  <section class="card card--front" aria-label="Voorzijde visitekaart">
    <div class="emblem" role="img" aria-label="Groot paardenhoofd-embleem, lichtgrijs watermerk"></div>
    <div class="card-details">
      <div class="brand"><span class="brand-dot"></span><span>Full Stable Care Vandorpe</span></div>
      <p class="person-name">Laurent Vandorpe</p>
      <p class="person-title">zaakvoerder</p>
      <p class="contact">
        + 32 491 68 27 04<br>
        fscvandorpe-example.eu<br>
        laurent@fscvandorpe-example.eu
      </p>
      <p class="company">
        <strong>Full Stable Care Vandorpe GCV</strong><br>
        Molkenweg 47, B - 2820 Bonheiden, België
      </p>
    </div>
  </section>
</body>
</html>
```